依頼概要
「月見そら堂」は川越の蔵通りに佇み、熟練の和菓子職人がつくる豆菓子を専門に販売しています。創業から70年にわたり、手技による和菓子の技術と希少な地域食材を大切にしながら一粒一粒の豆の美味しさを守っています。
ブランドに関するその他情報やトンマナについては添付資料をご確認ください。

https://tsukimi-soradou.com/

<制作物>
A1ポスター
※採用者には追加で「横断幕」や「展示POP」等の制作を依頼させて頂きます。

<特徴>
①和菓子職人による手技で仕上げた希少な和菓子
②豆にこだわり、100種を超える豆菓子を製造し販売している
③和菓子の町でもある小江戸川越の歴史と文化を受け継いでいる
④「グルテンフリー」または「ローグルテン」の体に優しい菓子

<今施策のターゲット>
①日本文化に対して興味関心の高い「海外モダンラグジュアリー層」
②東南アジアに住む富裕層
③東南アジアで飲食店等を営み「上質で希少な甘味」を求める事業者

<主力商品>
①きなこまめ
月見そら堂の伝統和菓子。完熟空豆を一週間かけて蜜漬けを繰り返したお多福豆。豊潤で濃厚な和菓子の美味しさを味わえる。秩父産の幻の大豆「福寄せ大豆」を使用したきなこが、香ばしさを加える。

<依頼詳細>
海外展示会で使用する「ポスター」の制作をお願いします。
展示会への来場者が外国人となるため、使用する主言語は「英語」としてください。
採用者には

①ポスター
専門店感や多商品感(バラエティー感)の表現を1枚で行うのが難しい場合には、複数数のシリーズ化でのデザイン提案も可(最大5枚の展示が可能)
※基本的には1デザインの制作で問題ありません。

サイズ:A1(縦長)
訴求内容:豆菓子専門店、きなこまめ、伝統的な高級和菓子、グルテンフリー、健康食
シズル感:きなこまめからのシズル感
商品情報等:添付資料(Product)を参照

※その他注意点
ご納品方法:入稿データでの納品としてください。
入稿データのルールやテンプレートは下記URLよりご確認お願いします。

印刷会社 ポスター:ランプレス
https://www.lanpress.jp/lineup/poster

記載項目
ブランド名:Tsukimi Soradou
会社名: Hirata Co., Ltd.
ロゴ:添付ファイル
サイズ(ポスター):A1縦
サイズ(横断幕):幅2100mm 高900mm

添付資料
①Leaflet → ブランドに関する情報やトンマナを確認いただける資料
②Product → ロゴ・写真等の素材
③Others → その他素材
※納品データ制作時に高解像度のデータを提出いたします。

その他にも素材はありますので、必要素材がありましたらお知らせください。

-----追加で依頼をお願いする制作物例----
のぼり横断幕
採用となるデザインパターンは1種のみ。展示可能箇所が1か所のみとなるため、シリーズ化のデザインは不可。

サイズ:幅2100mm 高900mm
生地:テトロンポンジ
シズル感:きなこまめからのシズル感
その他:可能であれば店舗外観を挿入(国内店舗との関連想起を促すため)

海外展示会での使用に対してのバランス感の良さを評価させて頂きました。
また、参考資料とさせていただいたリーフレットとの融和性も高く、海外におけるブランディング構築効果が高いと判断させて頂きました。

ご提案して頂きました皆様、誠にありがとうございます。
選考上での修正につきましても迅速な対応をしていただけたこと、重ねて御礼申し上げます。
最後まで選出に苦慮するほどに素敵なご提案が多く、社員一同感激しております。
別の機会がございましたら、何卒、宜しくお願い致します。

```html
<!DOCTYPE html>
<html lang="en">
<head>
<meta charset="utf-8">
<title>Tsukimi Soradou — Bean sweets specialty store</title>
<link rel="stylesheet" href="https://fonts.googleapis.com/css2?family=EB+Garamond:ital@0;1&family=Shippori+Mincho:wght@500&display=swap">
<style>
  :root {
    --paper: #ffffff;
    --ink: #2b2623;
    --ink-soft: #5a524c;
    --kinako-light: #e9cf9f;
    --kinako-deep: #c99e5c;
    --bean-dark: #2a1416;
    --bean-mid: #4a2a2c;
    --red-bean: #9c3b2e;
    --orange-bean: #d9653a;
    --amber-bean: #d4912f;
    --green-bean: #8e9a4a;
    --pink-bean: #d9968a;
    --cream-bean: #e3cba1;
    --maroon-bean: #6e2630;
    --speckle-bean: #b48a78;
  }
  * { margin: 0; padding: 0; box-sizing: border-box; }
  html, body { width: 849px; height: 1200px; overflow: hidden; background: var(--paper); }
  .poster {
    position: relative;
    width: 849px;
    height: 1200px;
    overflow: hidden;
    background: var(--paper);
    font-family: "EB Garamond", "Times New Roman", serif;
    color: var(--ink);
  }
  .label { position: absolute; font-size: 17px; letter-spacing: 0.02em; white-space: nowrap; }
  .brand-wordmark { left: 140px; top: 46px; font-size: 19px; }
  .brand-vertical {
    position: absolute;
    left: 262px;
    top: 92px;
    writing-mode: vertical-rl;
    font-family: "Shippori Mincho", serif;
    font-weight: 500;
    font-size: 40px;
    line-height: 1;
    letter-spacing: 0.08em;
    color: var(--ink);
  }
  .tagline-store { left: 500px; top: 48px; }
  .tagline-gluten { left: 640px; top: 282px; }
  .tagline-health { left: 50px; top: 635px; }
  .product-caption {
    left: 575px; top: 712px;
    font-size: 10px; line-height: 1.25; text-align: center; color: var(--ink-soft);
  }
  .company { left: 0; right: 0; top: 1112px; text-align: center; font-size: 22px; }

  .bean { position: absolute; border-radius: 50%; }
  .kinako-powder {
    position: absolute; left: 212px; top: 345px; width: 440px; height: 230px;
    border-radius: 50% 50% 46% 46% / 60% 60% 40% 40%;
    background: radial-gradient(ellipse at 50% 55%, var(--kinako-deep) 0%, var(--kinako-light) 55%, rgba(233,207,159,0) 75%);
  }
  .kinako-mame {
    position: absolute; left: 215px; top: 740px; width: 400px; height: 345px;
    border-radius: 48% 44% 50% 46% / 40% 42% 58% 60%;
    background: radial-gradient(ellipse at 40% 35%, var(--bean-mid) 0%, var(--bean-dark) 65%);
  }
</style>
</head>
<body>
<main class="poster">
  <p class="label brand-wordmark">tsukimi soradou</p>
  <h1 class="brand-vertical">月見そら堂</h1>

  <p class="label tagline-store">Bean sweets specialty store.</p>
  <p class="label tagline-gluten">gluten-free.</p>
  <p class="label tagline-health">healthy foods.</p>

  <div class="kinako-powder" role="img" aria-label="Pile of roasted soybean kinako powder"></div>
  <div class="kinako-mame" role="img" aria-label="Two glossy syrup-soaked broad beans, Kinako Mame"></div>

  <p class="label product-caption">Sweetened Kinako<br>"Kinako Mame"</p>

  <div class="bean" role="img" aria-label="Red-brown bean sweets" style="left:54px;top:32px;width:50px;height:50px;background:var(--red-bean)"></div>
  <div class="bean" role="img" aria-label="Amber bean sweets" style="left:402px;top:38px;width:42px;height:40px;background:var(--amber-bean)"></div>
  <div class="bean" role="img" aria-label="Golden soybean sweets" style="left:742px;top:30px;width:52px;height:52px;background:var(--amber-bean)"></div>

  <div class="bean" role="img" aria-label="Mixed dark bean sweets" style="left:570px;top:165px;width:58px;height:48px;background:var(--maroon-bean)"></div>
  <div class="bean" role="img" aria-label="Orange bean sweets" style="left:54px;top:262px;width:54px;height:54px;background:var(--orange-bean)"></div>
  <div class="bean" role="img" aria-label="Pink bean sweets" style="left:402px;top:262px;width:56px;height:46px;background:var(--pink-bean)"></div>
  <div class="bean" role="img" aria-label="Orange bean sweets" style="left:742px;top:258px;width:54px;height:54px;background:var(--orange-bean)"></div>
  <div class="bean" role="img" aria-label="Glazed amber bean sweet" style="left:58px;top:505px;width:40px;height:38px;background:var(--amber-bean)"></div>
  <div class="bean" role="img" aria-label="Red kidney bean sweets" style="left:742px;top:500px;width:60px;height:54px;background:var(--maroon-bean)"></div>
  <div class="bean" role="img" aria-label="Green bean sweets" style="left:222px;top:628px;width:50px;height:46px;background:var(--green-bean)"></div>
  <div class="bean" role="img" aria-label="Speckled bean sweets" style="left:570px;top:628px;width:54px;height:52px;background:var(--speckle-bean)"></div>
  <div class="bean" role="img" aria-label="Pink bean sweets" style="left:54px;top:732px;width:56px;height:50px;background:var(--pink-bean)"></div>
  <div class="bean" role="img" aria-label="Orange bean sweets" style="left:742px;top:740px;width:56px;height:50px;background:var(--orange-bean)"></div>
  <div class="bean" role="img" aria-label="Cream bean sweets" style="left:54px;top:880px;width:54px;height:52px;background:var(--cream-bean)"></div>
  <div class="bean" role="img" aria-label="Orange bean sweets" style="left:742px;top:880px;width:56px;height:52px;background:var(--orange-bean)"></div>
  <div class="bean" role="img" aria-label="Yellow bean sweets" style="left:58px;top:1000px;width:50px;height:46px;background:var(--cream-bean)"></div>
  <div class="bean" role="img" aria-label="Dark bean sweets" style="left:742px;top:990px;width:54px;height:50px;background:var(--bean-mid)"></div>
  <div class="bean" role="img" aria-label="Chickpea sweets" style="left:215px;top:1098px;width:54px;height:50px;background:var(--cream-bean)"></div>
  <div class="bean" role="img" aria-label="Orange bean sweets" style="left:580px;top:1100px;width:54px;height:46px;background:var(--orange-bean)"></div>
  <div class="bean" role="img" aria-label="Amber bean sweets" style="left:742px;top:1100px;width:54px;height:50px;background:var(--amber-bean)"></div>

  <p class="label company">Hirata Co., Ltd.</p>
</main>
</body>
</html>
```